New Advertising Company Business Card

A two sided business card. One side with logo only and the other side with my information and maybe my logo again. Looking for something unique and creative, but not too busy. Info would include my name(Marcus Feldon), President, phone number, address, email address, and website. LOGO IS THE BLUE AND WHITE ONE.

Target Market(s)

CEO/VP Level Audience

Industry/Entity Type

Business

Contact Information for Business Card

In Description.

```html
<!DOCTYPE html>
<html lang="en">
<head>
<meta charset="utf-8">
<title>Lumenar Advertising – Business Card</title>
<link href="https://fonts.googleapis.com/css2?family=Ubuntu:wght@400;500;700&display=swap" rel="stylesheet">
<style>
  :root {
    --brand-blue: #0a6dba;
    --brand-blue-deep: #085fa3;
    --ink: #111111;
    --paper: #ffffff;
    --stage: #ebebeb;
  }
  * { margin: 0; padding: 0; box-sizing: border-box; }
  html, body {
    width: 1200px; height: 960px; overflow: hidden;
    background: var(--stage);
    font-family: "Ubuntu", sans-serif;
  }
  .canvas { position: relative; width: 1200px; height: 960px; }

  /* Front side */
  .card-front {
    position: absolute; left: 265px; top: 67px;
    width: 673px; height: 385px; background: var(--paper); overflow: hidden;
  }
  .front-band {
    position: absolute; left: 0; top: 216px; width: 100%; height: 149px;
    background: var(--brand-blue);
  }
  .front-base {
    position: absolute; left: 0; bottom: 0; width: 100%; height: 20px;
    background: var(--ink);
  }
  .band-pointer { position: absolute; left: 387px; top: 216px; }
  .wordmark {
    position: absolute; color: var(--brand-blue); font-weight: 700;
    text-transform: uppercase; line-height: 1.05;
  }
  .card-front .wordmark { left: 36px; top: 110px; font-size: 40px; letter-spacing: 3px; }
  .card-front .wordmark small { display: block; font-size: 24px; letter-spacing: 6px; font-weight: 700; }
  .holder { position: absolute; left: 391px; top: 133px; }
  .holder-name { font-size: 22px; font-weight: 700; color: var(--ink); }
  .holder-role { font-size: 18px; color: var(--brand-blue); margin-top: 3px; }
  .address {
    position: absolute; left: 27px; top: 295px;
    color: var(--paper); font-size: 18px; line-height: 23px;
  }
  .contacts { position: absolute; left: 391px; top: 264px; list-style: none; }
  .contacts li {
    display: flex; align-items: center; gap: 9px;
    color: var(--paper); font-size: 18px; height: 25.5px;
  }
  .contacts svg { width: 20px; height: 20px; flex: none; }

  /* Back side */
  .card-back {
    position: absolute; left: 265px; top: 507px;
    width: 672px; height: 384px; background: var(--brand-blue); overflow: hidden;
  }
  .map-area {
    position: absolute; left: 22px; top: 32px; width: 636px; height: 314px;
    background: radial-gradient(ellipse at center, var(--brand-blue-deep) 0%, var(--brand-blue) 75%);
    opacity: .9;
  }
  .card-back .wordmark {
    left: 0; width: 100%; top: 170px; text-align: center;
    color: var(--paper); font-size: 50px; letter-spacing: 4px;
  }
  .card-back .wordmark small { display: block; font-size: 26px; letter-spacing: 7px; }
  .back-web {
    position: absolute; left: 0; width: 100%; top: 343px;
    display: flex; justify-content: center; align-items: center; gap: 10px;
    color: var(--paper); font-size: 16px;
  }
  .back-web .rule { width: 130px; height: 2px; background: var(--paper); }
</style>
</head>
<body>
<main class="canvas">
  <section class="card-front" aria-label="Business card front">
    <div class="wordmark">Lumenar<small>Advertising</small></div>
    <div class="holder">
      <p class="holder-name">Marcus Feldon</p>
      <p class="holder-role">President</p>
    </div>
    <div class="front-band"></div>
    <svg class="band-pointer" width="30" height="20" viewBox="0 0 30 20" aria-hidden="true">
      <polygon points="0,0 30,0 15,20" fill="#ffffff"/>
    </svg>
    <p class="address">2870 Alder Row,<br>Houston, TX 77024</p>
    <ul class="contacts">
      <li>
        <svg viewBox="0 0 20 20" aria-hidden="true"><rect width="20" height="20" fill="#111"/>
          <path d="M4 8c0-2 3-3 6-3s6 1 6 3l-2 1-1-2H7L6 9z M6 10h8l1 5H5z" fill="#fff"/></svg>
        555 218 4096
      </li>
      <li>
        <svg viewBox="0 0 20 20" aria-hidden="true"><rect width="20" height="20" fill="#111"/>
          <rect x="3.5" y="5.5" width="13" height="9" fill="none" stroke="#fff" stroke-width="1.5"/>
          <path d="M3.5 5.5L10 11l6.5-5.5" fill="none" stroke="#fff" stroke-width="1.5"/></svg>
        info@lumenaradvertising.com
      </li>
      <li>
        <svg viewBox="0 0 20 20" aria-hidden="true"><rect width="20" height="20" fill="#111"/>
          <circle cx="10" cy="10" r="6.5" fill="none" stroke="#fff" stroke-width="1.3"/>
          <ellipse cx="10" cy="10" rx="3" ry="6.5" fill="none" stroke="#fff" stroke-width="1.1"/>
          <path d="M3.5 10h13M5 6.5h10M5 13.5h10" stroke="#fff" stroke-width="1"/></svg>
        www.lumenaradvertising.com
      </li>
    </ul>
    <div class="front-base"></div>
  </section>

  <section class="card-back" aria-label="Business card back">
    <div class="map-area" role="img" aria-label="Dotted world map pattern in a slightly darker blue"></div>
    <div class="wordmark">Lumenar<small>Advertising</small></div>
    <div class="back-web"><span class="rule"></span>www.lumenaradvertising.com<span class="rule"></span></div>
  </section>
</main>
</body>
</html>
```